Corporate Intelligence Agency seeks redesign *

Varnholt Insight is a business intelligence firm made up of former special operations and intelligence professionals. Our vibe is quiet professionals that get the job done by whatever means necessary.
Our aesthetic is clean, sleek, and monochromatic. We prefer the texture contrasts over colors. Slick white or black, playing up textures, and bold block lettering, and simplicity are what we are looking for in a design.

The logo would preferably pay homage to our military/special operations roots, and the culture of changing for the better (alchemy) that we embody all while remaining simple.

Target Market(s)

C-Level executives with a taste for the simple over the extravagant, and cut right to the chase

Industry/Entity Type

Management Solution

Contact Information for Business Card

Back is matte black with a glossy black logo to contrast. The front has the logo, with space on the bottom left for name and contact

Logo Text

Varnholt Ins.

Logo styles of interest
Abstract Logo
Wordmark Logo
Lettermark Logo
Font styles to use
Serif
Sans Serif
Script

Requirements
Must have
• Monochromatic, play on texture within card (the card ought to be memorable to hold), solid/clean lettering. Logo should be simple and sleek.
Nice to have
• If the logo can tie alchemy and intelligence/spy genre. 3d textures
Should not have
• Nothing overtly military. No colors outside of the monochromatic spectrum

```html
<!DOCTYPE html>
<html lang="en">
<head>
<meta charset="utf-8">
<title>Varnholt Insight — Business Card</title>
<link rel="stylesheet" href="https://fonts.googleapis.com/css2?family=Source+Code+Pro:ital,wght@0,400;0,700;1,400;1,700&display=swap">
<style>
  :root {
    --backdrop: #b9babc;
    --card-front: #e8e9eb;
    --card-back: #3e3b3d;
    --ink: #1c1c1d;
    --ink-soft: #2e2e30;
    --mark-grey: #8d8d8f;
    --rule: #2a2a2b;
  }
  * { box-sizing: border-box; margin: 0; padding: 0; }
  html, body {
    width: 1200px; height: 1200px; overflow: hidden;
    background: var(--backdrop);
    font-family: "Source Code Pro", monospace;
  }
  .stage { position: relative; width: 1200px; height: 1200px; }

  .card { position: absolute; width: 600px; height: 370px; }
  .card--front {
    left: 262px; top: 170px;
    background:
      repeating-linear-gradient(0deg, rgba(0,0,0,0.025) 0 1px, transparent 1px 3px),
      var(--card-front);
  }
  .card--back {
    left: 280px; top: 660px;
    background:
      repeating-linear-gradient(0deg, rgba(255,255,255,0.03) 0 1px, transparent 1px 3px),
      var(--card-back);
  }

  .brand {
    position: absolute; display: flex; align-items: center; gap: 12px;
    font-weight: 700; color: var(--ink); white-space: nowrap;
  }
  .brand__dot { border-radius: 50%; background: currentColor; flex: none; }
  .card--front .brand { left: 44px; top: 120px; font-size: 24px; }
  .card--front .brand__dot { width: 22px; height: 22px; }
  .card--back .brand {
    left: 0; right: 0; top: 0; bottom: 0; justify-content: center;
    color: var(--mark-grey); font-size: 50px; gap: 20px;
  }
  .card--back .brand__dot { width: 44px; height: 44px; }

  .holder { position: absolute; left: 336px; top: 212px; color: var(--ink); }
  .holder__name { font-size: 21px; font-weight: 700; font-style: italic; letter-spacing: 0.5px; }
  .holder__role { font-size: 11.5px; margin-top: 3px; color: var(--ink-soft); }

  .contact {
    position: absolute; left: 336px; display: flex; align-items: center; gap: 12px;
    font-size: 13.5px; font-style: italic; color: var(--ink);
  }
  .contact--phone { top: 275px; }
  .contact--web { top: 326px; }
  .contact__icon { width: 26px; height: 26px; flex: none; }
  .contact-rule {
    position: absolute; left: 336px; top: 312px; width: 256px; height: 1.5px;
    background: var(--rule);
  }
</style>
</head>
<body>
<main class="stage">
  <section class="card card--front" aria-label="Business card front">
    <div class="brand"><span class="brand__dot"></span>Varnholt Ins.</div>

    <div class="holder">
      <p class="holder__name">Darian Kestrel</p>
      <p class="holder__role">Regional Security Officer (RSO)</p>
    </div>

    <div class="contact contact--phone">
      <svg class="contact__icon" viewBox="0 0 26 26" aria-hidden="true">
        <circle cx="13" cy="13" r="13" fill="var(--ink)"/>
        <path d="M9.2 6.8c.6-.4 1.3-.2 1.6.4l1.1 2.1c.3.6.1 1.2-.4 1.6l-.8.6c.6 1.6 1.6 2.8 3 3.6l.7-.7c.5-.5 1.2-.6 1.7-.2l1.9 1.3c.5.4.6 1.1.2 1.6l-.9 1.2c-.6.7-1.6 1-2.5.6-3.4-1.4-5.9-4.3-6.9-7.9-.3-.9 0-1.8.8-2.3z" fill="var(--card-front)"/>
      </svg>
      <span>555 014 2290</span>
    </div>
    <div class="contact-rule"></div>
    <div class="contact contact--web">
      <svg class="contact__icon" viewBox="0 0 26 26" aria-hidden="true">
        <circle cx="13" cy="13" r="13" fill="var(--ink)"/>
        <g fill="none" stroke="var(--card-front)" stroke-width="1.2">
          <circle cx="13" cy="13" r="8"/>
          <ellipse cx="13" cy="13" rx="3.5" ry="8"/>
          <path d="M5 13h16M6.5 9h13M6.5 17h13"/>
        </g>
      </svg>
      <span>varnholtinsight.com</span>
    </div>
  </section>

  <section class="card card--back" aria-label="Business card back">
    <div class="brand"><span class="brand__dot"></span>Varnholt Ins.</div>
  </section>
</main>
</body>
</html>
```